PVQ BOOK COVER 6 X 9 - MARKET LEADING LEADERSHIP BOOK

I need a book cover designed for a book called Steering Through the Era of Circuits – Enduring Insight for an Automated Century and some more stuff, which you can see in the image I generated. I created a basic cover, but it needs to wow; it's about leadership, ancient wisdom, and AI. This book offers a unique approach: combining 2,000-year-old Stoic philosophy with practical frameworks for modern AI-age leadership challenges. Rather than another technical book about AI, this is a deeply human guide for leaders who want to harness AI's power while preserving their organisation's humanity.

Target Market(s)

EXECUTIVES, LEADERS MANAGERS DEALING WITH AI

Industry/Entity Type

LEADERSHIP

Requirements
Must have
• MUSIC BE CLASSY AND A SOLID COMBINATION OF ANCIENT WISDOM AND FUTURISTIC AI
Nice to have
• GIVE ME THE BEST YOU HAVE
Should not have
• NON

```html
<!DOCTYPE html>
<html lang="en">
<head>
<meta charset="utf-8">
<title>Steering Through the Era of Circuits – Book Cover</title>
<link href="https://fonts.googleapis.com/css2?family=Cinzel:wght@400;600&family=Cormorant+Garamond:ital,wght@1,500&family=Montserrat:wght@500;700&display=swap" rel="stylesheet">
<style>
  :root {
    --page: #ffffff;
    --navy-deep: #1b3466;
    --navy-mid: #224a85;
    --navy-glow: #2f73b3;
    --ivory: #ffffff;
    --gold-light: #fbe97f;
    --gold-mid: #f0c94a;
    --gold-deep: #e2ab3c;
    --band-light: #f1dc93;
    --ink: #111111;
    --rule: rgba(255,255,255,0.75);
  }
  * { margin: 0; padding: 0; box-sizing: border-box; }
  html, body {
    width: 1200px; height: 1200px; overflow: hidden;
    background: var(--page);
  }
  .cover {
    position: absolute; left: 220px; top: 26px;
    width: 769px; height: 1156px; overflow: hidden;
    background:
      radial-gradient(ellipse 420px 360px at 50% 55%, var(--navy-glow) 0%, var(--navy-mid) 45%, transparent 80%),
      var(--navy-deep);
    text-align: center;
  }
  .title { font-weight: 400; }
  .title-top {
    position: absolute; top: 49px; left: 0; width: 100%;
    font-family: "Cinzel", serif; font-weight: 400;
    font-size: 132px; line-height: 1; color: var(--ivory);
    letter-spacing: -2px;
  }
  .connector {
    position: absolute; top: 174px; left: 0; width: 100%;
    display: flex; align-items: center; justify-content: center; gap: 26px;
    font-family: "Cormorant Garamond", serif; font-style: italic; font-weight: 500;
    font-size: 54px; color: var(--ivory);
  }
  .connector .rule {
    width: 140px; height: 2px;
    background: linear-gradient(90deg, transparent, var(--rule));
  }
  .connector .rule.right { background: linear-gradient(90deg, var(--rule), transparent); }
  .title-gold {
    position: absolute; left: 0; width: 100%;
    font-family: "Cinzel", serif; font-weight: 400; line-height: 1;
    background: linear-gradient(180deg, var(--gold-light) 0%, var(--gold-mid) 55%, var(--gold-deep) 100%);
    -webkit-background-clip: text; background-clip: text; color: transparent;
  }
  .title-gold.line-one { top: 234px; font-size: 116px; }
  .title-gold.line-two { top: 330px; font-size: 104px; letter-spacing: -1px; }
  .title-gold .small-word {
    font-family: "Cormorant Garamond", serif; font-style: italic;
    font-size: 58px; vertical-align: 30px; margin: 0 10px;
  }
  .artwork {
    position: absolute; left: 25px; top: 440px; width: 744px; height: 295px;
    border-radius: 140px 0 0 140px;
    background: radial-gradient(ellipse at 45% 50%, #d9d9dc 0%, #a7aab2 40%, #5c6f93 75%, transparent 100%);
    opacity: 0.55;
  }
  .subtitle {
    position: absolute; top: 733px; left: 0; width: 100%;
    font-family: "Montserrat", sans-serif; font-weight: 500;
    font-size: 27px; line-height: 42px; letter-spacing: 6px;
    color: var(--ivory);
  }
  .gold-band {
    position: absolute; top: 841px; left: 0; width: 100%; height: 177px;
    background: linear-gradient(90deg, var(--gold-deep) 0%, var(--band-light) 50%, var(--gold-deep) 100%);
    display: flex; align-items: center; justify-content: center;
    font-family: "Montserrat", sans-serif; font-weight: 700;
    font-size: 26px; line-height: 37.5px; letter-spacing: 3.5px;
    color: var(--ink);
  }
  .author {
    position: absolute; top: 1050px; left: 0; width: 100%;
    font-family: "Cinzel", serif; font-weight: 600;
    font-size: 58px; line-height: 1; letter-spacing: 4px;
    color: var(--ivory);
  }
</style>
</head>
<body>
  <main class="cover">
    <h1 class="title">
      <span class="title-top">STEERING</span>
      <span class="connector"><span class="rule"></span>through the<span class="rule right"></span></span>
      <span class="title-gold line-one">ERA<span class="small-word">of</span></span>
      <span class="title-gold line-two">CIRCUITS</span>
    </h1>

    <div class="artwork" role="img" aria-label="Illustration of a white robotic hand holding an open antique book"></div>

    <p class="subtitle">ENDURING INSIGHT FOR<br>AN AUTOMATED CENTURY</p>

    <p class="gold-band">STOIC DISCIPLINE,<br>MORAL FOCUS, AND HUMANE<br>GUIDANCE IN THE ERA<br>OF THINKING MACHINES</p>

    <p class="author">MARCUS VERELLE</p>
  </main>
</body>
</html>
```